Building Company Business Card Design

Need a design for a business card:
It needs to have: Name, Phone, Facebook link, Website, email
i would also like a list of works we undertake:
-New Homes
-Extensions, Renovations & Bathrooms
-Decking, Carports, Sheds (Residential and Industrial)
-Carpentry
-Fences, Patios & Pergolas

Name, Phone, Facebook link, Website, email + details of services provided listed in description

```html
<!DOCTYPE html>
<html lang="en">
<head>
<meta charset="utf-8">
<title>Keystone Building Co – Business Card</title>
<link href="https://fonts.googleapis.com/css2?family=Montserrat:wght@500;600;700&family=Lato:wght@400;700&display=swap" rel="stylesheet">
<style>
  :root {
    --backdrop: #3d3d3d;
    --card-dark: #121212;
    --card-light: #ffffff;
    --band: #efefef;
    --green: #2fb34a;
    --ink: #222222;
  }
  * { box-sizing: border-box; margin: 0; padding: 0; }
  html, body { width: 1200px; height: 1000px; overflow: hidden; }
  body { background: var(--backdrop); position: relative; font-family: "Lato", sans-serif; color: var(--ink); }

  .card { position: absolute; left: 191px; width: 817px; height: 467px; border-radius: 22px; overflow: hidden; box-shadow: 0 4px 14px rgba(0,0,0,.35); }
  .card-front { top: 24px; background: var(--card-dark); }
  .card-back { top: 508px; background: var(--card-light); }

  .front-name { position: absolute; left: 0; right: 0; top: 262px; text-align: center; font-family: "Montserrat", sans-serif; font-weight: 600; font-size: 38px; line-height: 44px; color: #ffffff; }

  .person { position: absolute; top: 34px; left: 0; right: 0; text-align: center; }
  .person-name { font-family: "Montserrat", sans-serif; font-weight: 600; font-size: 29px; color: var(--green); letter-spacing: .5px; line-height: 32px; }
  .person-title { font-size: 21px; margin-top: 2px; }

  .contact-band { position: absolute; top: 112px; left: 0; right: 0; height: 152px; background: var(--band); }
  .contact-list { list-style: none; position: absolute; left: 29px; top: 9px; }
  .contact-list li { display: flex; align-items: center; height: 32px; font-size: 19px; }
  .contact-list .icon { width: 22px; height: 22px; border-radius: 3px; background: var(--green); margin-right: 11px; display: flex; align-items: center; justify-content: center; }

  .brand-box { position: absolute; right: 32px; top: 84px; width: 214px; height: 158px; background: #fff; border-radius: 14px; box-shadow: 0 2px 6px rgba(0,0,0,.18); display: flex; align-items: center; justify-content: center; font-family: "Montserrat", sans-serif; font-weight: 600; font-size: 17px; color: var(--ink); }

  .services { position: absolute; top: 302px; left: 0; right: 0; text-align: center; }
  .services-title { font-family: "Montserrat", sans-serif; font-weight: 700; font-size: 28px; line-height: 36px; }
  .services-title .accent { color: var(--green); }
  .services-row { display: flex; justify-content: center; align-items: center; font-size: 19px; height: 42px; }
  .services-row:first-of-type { margin-top: 15px; }
  .sep { margin: 0 14px; display: inline-flex; }
</style>
</head>
<body>

<section class="card card-front">
  <h1 class="front-name">KEYSTONE BUILDING CO</h1>
</section>

<section class="card card-back">
  <div class="person">
    <h2 class="person-name">DANIEL HART</h2>
    <p class="person-title">Managing Director</p>
  </div>

  <div class="contact-band">
    <ul class="contact-list">
      <li><span class="icon"><svg width="14" height="14" viewBox="0 0 24 24"><path fill="#fff" d="M6.6 10.8a15 15 0 0 0 6.6 6.6l2.2-2.2a1 1 0 0 1 1-.25 11.4 11.4 0 0 0 3.6.57 1 1 0 0 1 1 1V20a1 1 0 0 1-1 1A17 17 0 0 1 3 4a1 1 0 0 1 1-1h3.5a1 1 0 0 1 1 1c0 1.25.2 2.45.57 3.57a1 1 0 0 1-.25 1z"/></svg></span>044-987 654 321</li>
      <li><span class="icon"><svg width="14" height="14" viewBox="0 0 24 24"><path fill="#fff" d="M2 11 22 3l-4 18-6-5-3 3v-5l9-9-11 7z"/></svg></span>info@keystonebuild.com</li>
      <li><span class="icon"><svg width="16" height="16" viewBox="0 0 24 24" fill="none" stroke="#fff" stroke-width="2"><circle cx="12" cy="12" r="9"/><path d="M3 12h18M12 3c3 3 3 15 0 18M12 3c-3 3-3 15 0 18"/></svg></span>www.keystonebuild.com</li>
      <li><span class="icon"></span>@keystonebuild</li>
    </ul>
  </div>

  <div class="brand-box">KEYSTONE BUILDING CO</div>

  <div class="services">
    <h3 class="services-title"><span class="accent">SERVICES</span> PROVIDED</h3>
    <div class="services-row">
      <span>New Homes</span>
      <span class="sep"><svg width="16" height="34" viewBox="0 0 16 34"><path d="M8 0v9M8 25v9" stroke="#2fb34a" stroke-width="2"/><path d="M8 10 14 17 8 24 2 17z" fill="none" stroke="#2fb34a" stroke-width="2"/></svg></span>
      <span>Extensions, Renovations &amp; Bathrooms</span>
      <span class="sep"><svg width="16" height="34" viewBox="0 0 16 34"><path d="M8 0v9M8 25v9" stroke="#2fb34a" stroke-width="2"/><path d="M8 10 14 17 8 24 2 17z" fill="none" stroke="#2fb34a" stroke-width="2"/></svg></span>
      <span>Carpentry</span>
    </div>
    <div class="services-row">
      <span>Decking, Carports, Sheds (Residential and Industrial)</span>
      <span class="sep"><svg width="16" height="34" viewBox="0 0 16 34"><path d="M8 0v9M8 25v9" stroke="#2fb34a" stroke-width="2"/><path d="M8 10 14 17 8 24 2 17z" fill="none" stroke="#2fb34a" stroke-width="2"/></svg></span>
      <span>Fences, Patios &amp; Pergolas</span>
    </div>
  </div>
</section>

</body>
</html>
```